One Page Sales Flyer for Wireless Survey- Computer Hardware

I want a designer to create a one page 4 color sales slick to be given to our sales team to sell to the end customers. I would like a visual picture of a heat map so zavvix "heat map wireless" to get an idea of how that image should look.

```html
<!DOCTYPE html>
<html lang="en">
<head>
<meta charset="utf-8">
<title>Wireless Site Surveys – Sales Flyer</title>
<link href="https://fonts.googleapis.com/css2?family=Oswald:wght@600;700&family=Ubuntu:wght@500;700&family=Open+Sans:wght@400;600&display=swap" rel="stylesheet">
<style>
  :root{
    --navy:#1c3461;
    --sky:#3a9fd8;
    --deep-blue:#1f6fb5;
    --ink:#1e2a44;
    --body:#222;
    --frame:#d4d8dc;
    --mint-top:#f4fafc;
    --mint-bottom:#a9dde6;
    --note-bar:#4a6fba;
    --white:#fff;
  }
  *{box-sizing:border-box;margin:0;padding:0}
  html,body{width:975px;height:1200px;overflow:hidden;background:var(--frame)}
  .flyer{position:relative;width:975px;height:1200px;background:var(--frame);font-family:"Open Sans",sans-serif;color:var(--body)}
  .top-band{position:absolute;left:0;top:0;width:975px;height:510px;background:var(--navy)}
  .lower-panel{position:absolute;left:25px;top:510px;width:925px;height:672px;background:linear-gradient(180deg,var(--mint-top) 20%,var(--mint-bottom) 100%)}
  .headline{position:absolute;left:0;top:50px;width:975px;text-align:center;font-family:"Oswald",sans-serif;font-weight:700;color:#e9ecef;text-transform:uppercase;letter-spacing:1px}
  .headline span{display:block;line-height:1}
  .headline .l1,.headline .l2{font-size:56px;margin-bottom:4px}
  .headline .l3{font-size:64px}
  .info-panel{position:absolute;left:45px;top:240px;width:880px;height:494px;background:var(--sky);border:6px solid var(--white);box-shadow:0 0 0 1px #cfe6f3;overflow:hidden}
  .info-text{position:absolute;left:28px;top:24px;width:316px;color:var(--white)}
  .info-text h2{font-family:"Ubuntu",sans-serif;font-weight:700;font-size:22px;line-height:1.25;margin-bottom:8px}
  .info-text p{font-size:13px;line-height:1.45;text-align:justify}
  .info-text p.why{font-size:13.5px;line-height:1.5}
  .info-text h2.second{margin-top:20px}
  .heatmap{position:absolute;left:378px;top:28px;width:476px;height:424px;border:3px solid #e4e7ea;background:linear-gradient(180deg,#dfe2e5 0 12%,#7cc143 12% 88%,#e3e6e9 88%)}
  .why-heading{position:absolute;left:105px;top:755px;font-family:"Ubuntu",sans-serif;font-weight:700;font-size:23px;color:var(--deep-blue)}
  .reasons{position:absolute;left:105px;top:795px;width:505px;list-style:none;font-size:13.5px;line-height:1.4;color:var(--body)}
  .reasons li{position:relative;padding-left:22px;margin-bottom:6px;text-align:justify}
  .reasons li::before{content:"";position:absolute;left:0;top:4px;width:11px;height:11px;border-radius:50%;background:var(--deep-blue)}
  .divider{position:absolute;left:638px;top:770px;width:1px;height:335px;background:#9fb0c4}
  .targets-heading{position:absolute;left:662px;top:764px;font-family:"Oswald",sans-serif;font-weight:600;font-size:30px;color:var(--deep-blue);white-space:nowrap}
  .targets{position:absolute;left:662px;top:822px;list-style:none;font-family:"Ubuntu",sans-serif;font-weight:700;font-size:19px;color:#2f3b4c}
  .targets li{position:relative;padding-left:23px;height:30.6px;line-height:30.6px;white-space:nowrap}
  .targets li::before{content:"";position:absolute;left:0;top:10px;width:11px;height:11px;border-radius:50%;background:var(--deep-blue)}
  .brand{position:absolute;left:58px;top:1080px;display:flex;align-items:center;gap:14px}
  .brand-square{width:40px;height:40px;background:var(--sky)}
  .brand-name{font-family:"Ubuntu",sans-serif;font-weight:500;font-size:44px;letter-spacing:2px;color:#2b2d31}
  .contact{position:absolute;left:352px;top:990px;color:var(--ink);font-family:"Ubuntu",sans-serif;font-weight:700}
  .contact .phone{font-family:"Oswald",sans-serif;font-size:38px;line-height:1.1;letter-spacing:1px}
  .contact .email{font-size:21px;margin-top:6px}
  .contact .web{font-size:19px;margin-top:14px;letter-spacing:1px}
  .source-note{position:absolute;left:345px;top:1136px;width:600px;height:22px;background:var(--note-bar);color:var(--white);font-size:11px;font-weight:600;line-height:22px;padding-left:12px}
</style>
</head>
<body>
<div class="flyer">
  <div class="top-band"></div>
  <div class="lower-panel"></div>

  <h1 class="headline">
    <span class="l1">Increase Hardware and</span>
    <span class="l2">Services Spend with</span>
    <span class="l3">Wireless Site Surveys</span>
  </h1>

  <section class="info-panel">
    <div class="info-text">
      <h2>What is a wireless site survey or heat map?</h2>
      <p>A wireless site survey is a compilation of reports showing a visual representation of health of your wireless network. This does not only show how strong or weak a wireless signal is in any location it also helps aid in channel and placement to ensure maximum stable data rates are archived even where the single appears strong.</p>
      <h2 class="second">Why do customers need a site survey?</h2>
      <p class="why">Any variety of factors can contribute to an unhealthy wireless network (electrical, motors, materials used in construction, distance, neighboring wireless networks, etc.) and traditional methods that use only blueprints and a computer program to show signal strength have shown to be ineffective.</p>
    </div>
    <div class="heatmap" role="img" aria-label="Screenshot of a wireless network health heat map over an office floor plan, mostly green with a few red problem areas and callout notes"></div>
  </section>

  <h2 class="why-heading">Why should they use you?</h2>
  <ul class="reasons">
    <li>42% of businesses report some issues with wireless connectivity and acknowledge its effect on the bottom line*</li>
    <li>Most of these problems are solved through either fine tuning the current equipment (managed services) or purchasing new equipment (incremental sales) of which you can provide both</li>
    <li>Being a one-stop shop for all your customer’s IT needs prevents them from needing additional vendors</li>
    <li>The increase of IoT (Internet of things) and BYOD (Bring Your Own Device)</li>
  </ul>

  <div class="divider"></div>
  <h2 class="targets-heading">TARGET CUSTOMERS</h2>
  <ul class="targets">
    <li>Distributors</li>
    <li>Warehouses</li>
    <li>SLED</li>
    <li>K-12</li>
    <li>Medical / Hospitals</li>
    <li>Enterprise F1000</li>
    <li>Sports Venues</li>
    <li>Stadiums</li>
    <li>Hotels</li>
    <li>Retail stores</li>
  </ul>

  <div class="brand">
    <div class="brand-square"></div>
    <div class="brand-name">KESTREL</div>
  </div>

  <div class="contact">
    <div class="phone">555-014-2290</div>
    <div class="email">info@kestrelnet.com</div>
    <div class="web">www.kestrelnet.com</div>
  </div>

  <div class="source-note">*Newswire Daily. “Connectivity in the Modern Enterprise”. June 2017</div>
</div>
</body>
</html>
```